Frostwell Cool Bricks needs stationery designed for their new logo

We have a new logo so now want all our stationery to be redesigned.
Frostwell is a gel ice pack product used by the seafood & food industry to transport chilled products around the world.

We would like to use our new logo with icy or snow backgrounds or elements.
Our company tag line is "Cold that holds from dock to door"
I'll attach our old business cards so that you can use the text off them.
2nd attachment is our new logo to be used.

We want a design for:
- Business cards
- Letter Head
- Email signature

Target Market(s)

seafood & chilled food distributors

Industry/Entity Type

Industry

Font styles to use
Sans Serif

Colors
0492cd
85cae6
cee9f5

Requirements
Must have
• Our logo
Nice to have
• Snow or ice background or image incorporated somehow

```html
<!DOCTYPE html>
<html lang="en">
<head>
<meta charset="utf-8">
<title>Frostwell Business Card</title>
<link rel="stylesheet" href="https://fonts.googleapis.com/css2?family=Lato:wght@400;700;900&display=swap">
<style>
  :root {
    --brand-blue: #0492cd;
    --ice-mid: #85cae6;
    --ice-pale: #cee9f5;
    --logo-blue: #1f63c9;
    --text-grey: #5f6468;
    --rule-grey: #9aa0a4;
    --card-white: #ffffff;
    --stage: #e9ecee;
  }
  * { margin: 0; padding: 0; box-sizing: border-box; }
  html, body {
    width: 1200px; height: 900px; overflow: hidden;
    background: var(--stage);
    font-family: "Lato", sans-serif;
  }
  .canvas { position: relative; width: 1200px; height: 900px; }

  .card {
    position: absolute;
    width: 600px; height: 343px;
    background: var(--card-white);
    overflow: hidden;
    box-shadow: 0 6px 18px rgba(0,0,0,0.18);
  }
  .card--back { left: 110px; top: 90px; }
  .card--front { left: 490px; top: 467px; }

  .ice-field {
    position: absolute; top: 0; height: 100%;
    background:
      radial-gradient(ellipse at 30% 35%, rgba(255,255,255,0.55), transparent 45%),
      radial-gradient(ellipse at 65% 70%, rgba(206,233,245,0.7), transparent 50%),
      linear-gradient(160deg, #29a6dc 0%, var(--ice-mid) 35%, var(--brand-blue) 60%, var(--ice-mid) 85%, var(--ice-pale) 100%);
  }
  .card--back .ice-field {
    left: 0; width: 62%;
    -webkit-mask-image: linear-gradient(90deg, #000 60%, transparent 100%);
            mask-image: linear-gradient(90deg, #000 60%, transparent 100%);
  }
  .card--front .ice-field {
    right: 0; width: 62%;
    -webkit-mask-image: linear-gradient(270deg, #000 60%, transparent 100%);
            mask-image: linear-gradient(270deg, #000 60%, transparent 100%);
  }

  .brand { display: flex; align-items: center; gap: 10px; }
  .brand__dot { width: 30px; height: 30px; border-radius: 50%; background: var(--logo-blue); flex: none; }
  .brand__name { font-weight: 900; color: var(--logo-blue); letter-spacing: 0.5px; line-height: 1; }
  .brand__tagline { color: var(--logo-blue); font-size: 12px; margin-top: 4px; white-space: nowrap; }

  /* back */
  .back-info { position: absolute; right: 36px; top: 34px; width: 250px; }
  .back-info .brand__name { font-size: 32px; }
  .back-info .brand__tagline { padding-left: 40px; }
  .office { text-align: center; margin-top: 22px; }
  .office + .office { margin-top: 8px; }
  .office__city { color: var(--brand-blue); font-weight: 700; font-size: 13px; letter-spacing: 0.5px; }
  .office__address { color: var(--text-grey); font-size: 12.5px; line-height: 1.35; }
  .divider-icon { display: flex; align-items: center; gap: 8px; margin: 10px 22px 0; }
  .divider-icon::before, .divider-icon::after { content: ""; flex: 1; height: 1px; background: var(--rule-grey); }

  /* front */
  .front-info { position: absolute; left: 34px; top: 42px; width: 300px; }
  .front-info .brand__name { font-size: 42px; }
  .front-info .brand__tagline { font-size: 13px; padding-left: 40px; }
  .person { margin-top: 22px; padding-left: 70px; }
  .person__name { font-size: 22px; letter-spacing: 1px; color: var(--text-grey); }
  .person__name strong { color: var(--logo-blue); font-weight: 900; }
  .person__role { font-size: 15px; color: var(--text-grey); margin-top: 2px; letter-spacing: 0.5px; }
  .contact { margin-top: 8px; text-align: center; width: 300px; }
  .contact .divider-icon { margin: 8px 20px 6px; }
  .contact__line { font-size: 16px; color: var(--text-grey); letter-spacing: 0.3px; }
</style>
</head>
<body>
<main class="canvas">

  <section class="card card--back">
    <div class="ice-field" role="img" aria-label="Close-up photograph of blue crushed ice crystals"></div>
    <div class="back-info">
      <div class="brand">
        <span class="brand__dot"></span>
        <span class="brand__name">Frostwell</span>
      </div>
      <p class="brand__tagline">Cold that holds from dock to door</p>

      <div class="office">
        <p class="office__city">SYDNEY</p>
        <p class="office__address">14 Harbour Lane, North Sydney,<br>NSW 2060</p>
      </div>
      <div class="divider-icon">
        <svg width="12" height="16" viewBox="0 0 12 16" aria-hidden="true">
          <path d="M6 0C2.7 0 0 2.6 0 5.8 0 10 6 16 6 16s6-6 6-10.2C12 2.6 9.3 0 6 0z" fill="#0492cd"/>
          <circle cx="6" cy="5.8" r="2.2" fill="#fff"/>
        </svg>
      </div>
      <div class="office">
        <p class="office__city">AUCKLAND</p>
        <p class="office__address">21 Kauri Road, Silverdale<br>Auckland 0932</p>
      </div>
    </div>
  </section>

  <section class="card card--front">
    <div class="ice-field" role="img" aria-label="Close-up photograph of blue crushed ice crystals"></div>
    <div class="front-info">
      <div class="brand">
        <span class="brand__dot"></span>
        <span class="brand__name">Frostwell</span>
      </div>
      <p class="brand__tagline">Cold that holds from dock to door</p>

      <div class="person">
        <p class="person__name"><strong>MARCUS</strong> HALE</p>
        <p class="person__role">Business Development</p>
      </div>

      <div class="contact">
        <div class="divider-icon">
          <svg width="18" height="13" viewBox="0 0 18 13" aria-hidden="true">
            <rect x="0" y="0" width="18" height="13" rx="1.5" fill="#1f63c9"/>
            <path d="M1 1.2 9 7.5 17 1.2" fill="none" stroke="#fff" stroke-width="1.4"/>
          </svg>
        </div>
        <p class="contact__line">marcus.hale@frostwell.com.au</p>
        <div class="divider-icon">
          <svg width="18" height="18" viewBox="0 0 18 18" aria-hidden="true">
            <g fill="none" stroke="#1f63c9" stroke-width="1.4">
              <circle cx="9" cy="9" r="8"/>
              <ellipse cx="9" cy="9" rx="3.5" ry="8"/>
              <path d="M1 9h16M2.5 5h13M2.5 13h13"/>
            </g>
          </svg>
        </div>
        <p class="contact__line">www.frostwell.com.au</p>
      </div>
    </div>
  </section>

</main>
</body>
</html>
```